Website re-design wedding music business

I need my wordpress wedding music website redesigned. I'm a wedding pianist and also provide duo/trio entertainment with other musicians and looking for an overhaul of my wordpress site.

Website: tollykessing.com.au

Target Market(s)

brides; engaged couples

Industry/Entity Type

Wedding

Number of Pages Required

5+ page

Colors

Designer to choose colors to be used in the design.

Requirements
Must have
• I'm looking to overhaul my website which is looking rather tired after 4 years. It is functional but not inviting to visitors. Initially my website started out as a solo piano player providing music for wedding. It is gradually growing now where brides can book
• 1) Solo Piano
• 2) Duo (any combination of Piano / Cello / Vocalist / Violin)
• 3) Trio (any combination of Piano/ Cello /Vocalist / Violin)
• in future it may increase to 4 / 5 /6 piece bands so that needs to be taken into account for the future growth where I'll recruit other musicians.
• Some other functionality I'd like to see
• - Visitors want a calendar to know availability of musicians
• - Automatically providing enquiry price & discount (if applicable)
• - Automating the booking form process (manual) - There's a PDF form I send to the customer after we go back/forth on email on songs/price etc but if more of it could be automated online that would be great. If move to online it would be good to be able to override the set prices with a custom price and also providing a payment gateway
• More Flexibility on pricing - customer selects type of artists they want and it calculates a price based on who they have chosen whether it is a ceremony or canapes or reception (or combination of any). Extra transport fee is added if >50km out of Melbourne.
• How would you re-design this website. Imagine you are a bride/groom looking to book wedding music services. I would love to see some concepts .
• Please indicate any other fees required for your submission and level of support post this competition. I would like this to be an on-going relationship.
Nice to have
• I'd preferably like the website to be in wordpress as I've been familiar with it over time and can do basic updates in the back end. Happy for other suggestions if you can convince me I should move away from wordpress.

```html
<!DOCTYPE html>
<html lang="en">
<head>
<meta charset="utf-8">
<title>Tolly Kessing – Wedding Pianist</title>
<link rel="stylesheet" href="https://fonts.googleapis.com/css2?family=Roboto:wght@300;400;500;700;900&display=swap">
<style>
:root{
  --blue:#2f7ec4;
  --blue-dark:#1f5f9c;
  --blue-light:#5aa6e6;
  --ink:#111;
  --text:#444;
  --muted:#777;
  --dark:#1b1b1b;
  --dark-2:#2a2a2a;
  --white:#fff;
  --line:#d8d8d8;
  --light:#f3f3f3;
}
*{box-sizing:border-box;margin:0;padding:0}
html,body{width:1200px;height:4128px;overflow:hidden}
body{font-family:"Roboto",Arial,sans-serif;color:var(--text);background:var(--white);position:relative}
section,header,nav,footer{position:relative;width:1200px}

/* header */
.site-header{height:88px;background:var(--white);display:flex;align-items:center;justify-content:space-between;padding:0 160px}
.brand{display:flex;align-items:center;gap:14px;font-size:30px;color:var(--ink);letter-spacing:.5px;font-weight:400}
.brand-mark{width:54px;height:54px;border-radius:50%;background:var(--ink)}
.call{display:flex;align-items:center;gap:10px;color:var(--ink)}
.call small{display:block;font-size:14px;font-weight:500}
.call strong{font-size:26px;font-weight:500}

.main-nav{height:40px;background:var(--blue);display:flex;align-items:center;padding:0 160px}
.main-nav a{color:var(--white);text-decoration:none;font-size:13px;font-weight:500;padding:0 10px;height:40px;line-height:40px;text-transform:uppercase;white-space:nowrap;flex:none}
.main-nav a.active{background:var(--blue-dark)}

.hero{height:524px;background:linear-gradient(180deg,#6e8a4c 0%,#3f5a2e 55%,#2b3b22 100%)}

/* intro */
.intro{height:531px;display:flex;padding:58px 160px 0}
.intro-copy{width:525px;text-align:center;padding-top:20px}
.intro-copy h1{font-size:48px;font-weight:400;color:var(--ink);letter-spacing:2px}
.intro-copy .role{font-size:19px;letter-spacing:3px;color:var(--ink);margin-top:4px}
.badges{display:flex;justify-content:center;gap:34px;margin:34px 0 30px}
.badge{width:78px;height:78px;border-radius:50%;background:#c9a640}
.badge:first-child{background:#2c2c2c}
.badge:last-child{background:#cfd3da}
.intro-copy p{font-size:14px;line-height:1.6;color:var(--text);padding:0 40px}
.btn-dark{display:inline-flex;align-items:center;gap:10px;background:var(--ink);color:var(--white);font-size:15px;font-weight:700;padding:12px 20px;margin-top:28px;text-decoration:none}
.btn-dark i{width:22px;height:16px;border-radius:3px;background:var(--white);display:inline-block}
.enquiry{position:absolute;left:685px;top:58px;width:355px;height:424px;background:var(--blue);padding:22px 26px;color:var(--white);text-align:center}
.enquiry h2{font-weight:300;font-size:20px;line-height:1.1;white-space:nowrap}
.enquiry h2 span{display:block;font-size:28px;font-weight:400}
.field{height:36px;border:1px solid rgba(255,255,255,.6);margin-top:12px;font-size:11px;text-align:left;padding:0 12px;line-height:36px;color:#e6f0fa;position:relative}
.field.select::after{content:"";position:absolute;right:12px;top:15px;border:5px solid transparent;border-top-color:#fff}
.field.area{height:70px;line-height:28px}
.btn-send{display:inline-block;background:var(--ink);color:var(--white);font-size:14px;font-weight:500;padding:11px 22px;margin-top:22px}

/* services */
.services{height:468px;background:linear-gradient(180deg,#222 0%,#0d0d0d 100%);text-align:center;padding-top:40px}
.section-title{font-size:32px;font-weight:700;color:var(--white);letter-spacing:.5px}
.section-sub{font-size:14px;color:#ccc;margin-top:4px}
.service-cards{position:absolute;top:124px;left:160px;width:877px;height:303px}
.service{position:absolute;top:0;width:242px;height:303px;background:var(--blue);color:var(--white);padding-top:18px}
.service:nth-child(1){left:0}.service:nth-child(2){left:327px}.service:nth-child(3){left:635px}
.service .icon{width:100px;height:100px;border-radius:50%;background:var(--ink);margin:0 auto;display:flex;align-items:center;justify-content:center}
.service h3{font-size:14px;font-weight:700;margin-top:24px}
.service hr{width:34px;border:0;border-top:2px solid var(--white);margin:8px auto}
.service p{font-size:11px;line-height:1.4;padding:0 32px;color:#e2eef9}
.btn-more{display:inline-block;margin-top:18px;font-size:9px;font-weight:700;border:1px solid var(--white);background:var(--ink);padding:7px 10px}

/* prices */
.prices{height:597px;text-align:center;padding-top:38px}
.prices h2{font-size:40px;font-weight:700;color:var(--ink)}
.prices h2::after{content:"";display:block;width:40px;height:3px;background:var(--blue);margin:8px auto 0}
.prices .lead{font-size:11px;line-height:1.6;width:880px;margin:16px auto 0}
.price-cards{position:absolute;top:190px;left:160px;width:880px;height:347px}
.price{position:absolute;top:0;width:204px;height:347px;border:1px solid var(--line)}
.price:nth-child(1){left:0}.price:nth-child(2){left:225px}.price:nth-child(3){left:451px}.price:nth-child(4){left:676px}
.price-head{background:var(--ink);color:var(--white);height:76px;padding-top:12px}
.price-head small{display:block;font-size:12px}
.price-head strong{display:block;font-size:27px;font-weight:700;margin-top:4px}
.price .num{font-size:42px;font-weight:700;color:var(--ink);margin-top:16px;line-height:1}
.price .unit{font-size:27px;font-weight:700;color:var(--ink)}
.seal{width:90px;height:90px;margin:10px auto 0;position:relative}
.seal span{position:absolute;inset:0;display:flex;align-items:center;justify-content:center;color:var(--white);font-size:30px;font-weight:700}
.seal span sup{font-size:11px;margin-top:-6px}
.btn-book{display:inline-block;background:var(--ink);color:var(--white);font-size:15px;font-weight:700;padding:10px 20px;margin-top:14px}

/* events */
.events{height:655px;background:linear-gradient(180deg,#2d2d2d 0%,#0e0e0e 100%);padding-top:52px;text-align:center}
.events h2{font-size:44px;font-weight:700;color:var(--white)}
.events h2::after{content:"";display:block;width:40px;height:3px;background:var(--white);margin:8px auto 0}
.event-photo{position:absolute}
.event-card{position:absolute;background:var(--white);text-align:left;padding:20px 22px}
.event-card h3{font-size:13px;font-weight:700;color:var(--ink)}
.event-card p{font-size:11px;line-height:1.45;margin-top:10px}
.event-card time{display:block;font-size:10px;color:var(--muted);margin-top:10px}

/* calendar + player */
.media-row{height:372px;background:var(--white)}
.calendar{position:absolute;left:160px;top:40px;width:267px;height:270px;background:#c7dff3}
.cal-head{height:40px;background:var(--dark-2);color:var(--white);display:flex;align-items:center;justify-content:space-between;padding:0 12px;font-size:15px;font-weight:500}
.cal-head i{width:18px;height:18px;border-radius:50%;background:var(--white);display:inline-block}
.cal-grid{display:grid;grid-template-columns:repeat(7,1fr);gap:3px;padding:4px}
.cal-grid b{font-size:8px;text-align:center;color:#555;font-weight:500;padding:2px 0}
.cal-grid span{height:36px;background:var(--blue-light);color:var(--ink);font-size:12px;display:flex;align-items:center;justify-content:center}
.cal-grid span.off{background:#e8e8e8;color:#888}
.cal-grid span.on{background:var(--ink);color:var(--white)}
.player{position:absolute;left:611px;top:40px;width:429px;height:270px;background:var(--light);padding:22px 22px}
.track{display:flex;gap:12px;align-items:flex-start}
.play{width:34px;height:34px;border-radius:50%;background:#e8501f;position:relative;flex:none}
.play::after{content:"";position:absolute;left:13px;top:10px;border-left:11px solid #fff;border-top:7px solid transparent;border-bottom:7px solid transparent}
.track small{display:block;font-size:11px;color:var(--ink)}
.track em{display:block;font-style:normal;font-size:11px;color:#555;margin-top:12px}
.wave{margin-top:18px}
.volume{display:flex;align-items:center;gap:16px;margin-top:20px}
.volume .bar{flex:1;height:2px;background:#333;position:relative}
.volume .bar::after{content:"";position:absolute;left:68%;top:-6px;width:14px;height:14px;border-radius:50%;background:#333}

/* testimonials */
.testimonials{height:482px;border-top:5px solid var(--blue-light);text-align:center;padding-top:48px}
.testimonials h2{font-size:32px;font-weight:700;color:var(--ink)}
.testimonials h2::after{content:"";display:block;width:40px;height:3px;background:var(--blue);margin:6px auto 0}
.avatar{position:absolute;border-radius:50%;border:4px solid #e6e6e6}
.arrow{position:absolute;top:221px;width:28px;height:28px;border-radius:50%;background:#bbb}
.quote{position:absolute;top:380px;left:160px;width:880px;font-size:14px;font-style:italic;color:#333;white-space:nowrap}
.quote small{display:block;font-size:11px;color:var(--blue);margin-top:8px}

/* footer */
.site-footer{height:371px;background:linear-gradient(180deg,#2b2b2b,#151515);color:var(--white);text-align:center;padding-top:44px}
.site-footer h2{font-size:26px;font-weight:700;color:#ddd}
.share{display:flex;justify-content:center;gap:18px;margin-top:20px}
.share a{display:flex;align-items:center;gap:10px;width:176px;height:40px;border-radius:20px;color:var(--white);font-size:14px;font-weight:700;text-decoration:none;justify-content:center;position:relative}
.share a::before{content:"";position:absolute;left:8px;top:9px;width:22px;height:22px;border-radius:50%;background:rgba(0,0,0,.35)}
.share .s1{background:#3b5896}.share .s2{background:#1da9d8}.share .s3{background:#e0503a}
.tagline{color:var(--blue-light);font-size:14px;margin-top:30px}
.contacts{display:flex;justify-content:center;gap:40px;font-size:11px;margin-top:20px;color:#ddd}
.pin{margin-top:16px}
.address{font-size:11px;line-height:1.5;color:#ddd}
.legal{position:absolute;bottom:0;left:0;width:1200px;height:40px;display:flex;align-items:center;justify-content:space-between;padding:0 160px;font-size:9px;color:#ccc;border-top:1px solid #333;white-space:nowrap}
.legal nav{width:auto}
.legal nav a{color:#ccc;text-decoration:none;margin-right:16px;text-transform:uppercase}
</style>
</head>
<body>

<header class="site-header">
  <div class="brand"><span class="brand-mark"></span><span>TOLLY KESSING</span></div>
  <div class="call">
    <svg width="30" height="30" viewBox="0 0 24 24"><circle cx="12" cy="12" r="11" fill="none" stroke="#111" stroke-width="1.6"/><path d="M8 6.5l2 2-1.2 1.6a7 7 0 0 0 5.1 5.1l1.6-1.2 2 2-1.4 1.6c-4.6-.4-9.2-5-9.6-9.6z" fill="#111"/></svg>
    <div><small>Call Now!</small><strong>0400 518 372</strong></div>
  </div>
</header>

<nav class="main-nav">
  <a class="active" href="#">Home</a><a href="#">About Tolly</a><a href="#">Events</a><a href="#">Music</a><a href="#">Video</a><a href="#">Repertoire</a><a href="#">Prices</a><a href="#">Gallery</a><a href="#">Testimonials</a><a href="#">Buy CD</a><a href="#">FAQs</a><a href="#">Contact</a>
</nav>

<section class="hero" role="img" aria-label="Photo of a pianist at a white grand piano and a cellist standing outdoors among trees"></section>

<section class="intro">
  <div class="intro-copy">
    <h1>TOLLY KESSING</h1>
    <div class="role">Wedding Pianist | Event Pianist</div>
    <div class="badges"><span class="badge"></span><span class="badge"></span><span class="badge"></span></div>
    <p>Tolly Kessing is Melbourne's premier award wedding &amp; event pianist specialising in playing beautiful background music for weddings, special occasions &amp; corporate events</p>
    <a class="btn-dark" href="#"><i></i>BOOK NOW!</a>
  </div>
  <form class="enquiry">
    <h2>Arrange a consultation<span>OR MAKE AN ENQUIRY</span></h2>
    <div class="field">Enter your name</div>
    <div class="field">Enter your email</div>
    <div class="field select">Enter your price</div>
    <div class="field select">Enter your discount price</div>
    <div class="field area">Enter your message</div>
    <span class="btn-send">SEND ENQUIRY!</span>
  </form>
</section>

<section class="services">
  <h2 class="section-title">WEDDING MUSIC SERVICES</h2>
  <div class="section-sub">Wedding Pianist | Event Pianist</div>
  <div class="service-cards">
    <article class="service">
      <div class="icon"><svg width="48" height="40" viewBox="0 0 48 40"><rect x="2" y="2" width="44" height="36" fill="#fff"/><g fill="#111"><rect x="9" y="2" width="4" height="20"/><rect x="17" y="2" width="4" height="20"/><rect x="27" y="2" width="4" height="20"/><rect x="35" y="2" width="4" height="20"/></g><g stroke="#111" stroke-width="1.2"><line x1="15" y1="2" x2="15" y2="38"/><line x1="24" y1="2" x2="24" y2="38"/><line x1="33" y1="2" x2="33" y2="38"/><line x1="8" y1="22" x2="8" y2="38"/><line x1="40" y1="22" x2="40" y2="38"/></g></svg></div>
      <h3>SOLO PIANO</h3><hr>
      <p>Elegant piano pieces chosen for your ceremony, drinks and dinner, played live on the day.</p>
      <span class="btn-more">READ MORE ➜</span>
    </article>
    <article class="service">
      <div class="icon"><svg width="44" height="54" viewBox="0 0 44 54"><ellipse cx="22" cy="38" rx="11" ry="13" fill="#fff"/><ellipse cx="22" cy="20" rx="8" ry="9" fill="#fff"/><line x1="22" y1="2" x2="22" y2="50" stroke="#111" stroke-width="2"/><line x1="8" y1="50" x2="38" y2="6" stroke="#fff" stroke-width="2"/></svg></div>
      <h3>DUO</h3><hr>
      <p>Piano paired with cello, violin or vocals for a richer sound across your whole celebration.</p>
      <span class="btn-more">READ MORE ➜</span>
    </article>
    <article class="service">
      <div class="icon"><svg width="30" height="56" viewBox="0 0 30 56"><rect x="7" y="2" width="16" height="24" rx="8" fill="#fff"/><rect x="12" y="26" width="6" height="26" fill="#fff"/><line x1="7" y1="12" x2="23" y2="12" stroke="#111" stroke-width="1.5"/></svg></div>
      <h3>TRIO</h3><hr>
      <p>Three musicians in any mix of piano, strings and voice to fill a larger room with music.</p>
      <span class="btn-more">READ MORE ➜</span>
    </article>
  </div>
</section>

<section class="prices">
  <h2>PRICES</h2>
  <p class="lead">Lorem Ipsum is simply dummy text of the printing and typesetting industry. Lorem Ipsum has been the industry's standard dummy text ever since the 1500s, when an unknown printer took a galley of type and scrambled it to make a type specimen book. It was popularised in the 1960s with the release of Presstype sheets containing Lorem Ipsum passages, and more recently with desktop publishing software like Quill Layout including versions of Lorem Ipsum.</p>
  <div class="price-cards">
    <article class="price"><div class="price-head"><small>Wedding Ceremony</small><strong>MELBOURNE</strong></div><div class="num">1</div><div class="unit">HOUR(S)</div><div class="seal"><svg width="90" height="90" viewBox="0 0 90 90"><polygon fill="#2f7ec4" points="45,2 53,10 64,6 68,17 79,19 78,30 87,37 81,46 87,55 78,61 79,72 68,73 64,84 53,80 45,88 37,80 26,84 22,73 11,72 12,61 3,55 9,46 3,37 12,30 11,19 22,17 26,6 37,10"/></svg><span><sup>$</sup>300</span></div><span class="btn-book">Book Now!</span></article>
    <article class="price"><div class="price-head"><small>Canapés or Reception</small><strong>MELBOURNE</strong></div><div class="num">1</div><div class="unit">HOUR(S)</div><div class="seal"><svg width="90" height="90" viewBox="0 0 90 90"><polygon fill="#2f7ec4" points="45,2 53,10 64,6 68,17 79,19 78,30 87,37 81,46 87,55 78,61 79,72 68,73 64,84 53,80 45,88 37,80 26,84 22,73 11,72 12,61 3,55 9,46 3,37 12,30 11,19 22,17 26,6 37,10"/></svg><span><sup>$</sup>300</span></div><span class="btn-book">Book Now!</span></article>
    <article class="price"><div class="price-head"><small>Duo: Vocalist/Piano</small><strong>MELBOURNE</strong></div><div class="num">1</div><div class="unit">HOUR(S)</div><div class="seal"><svg width="90" height="90" viewBox="0 0 90 90"><polygon fill="#2f7ec4" points="45,2 53,10 64,6 68,17 79,19 78,30 87,37 81,46 87,55 78,61 79,72 68,73 64,84 53,80 45,88 37,80 26,84 22,73 11,72 12,61 3,55 9,46 3,37 12,30 11,19 22,17 26,6 37,10"/></svg><span><sup>$</sup>300</span></div><span class="btn-book">Book Now!</span></article>
    <article class="price"><div class="price-head"><small>Violin or Cello</small><strong>MELBOURNE</strong></div><div class="num">1</div><div class="unit">HOUR(S)</div><div class="seal"><svg width="90" height="90" viewBox="0 0 90 90"><polygon fill="#2f7ec4" points="45,2 53,10 64,6 68,17 79,19 78,30 87,37 81,46 87,55 78,61 79,72 68,73 64,84 53,80 45,88 37,80 26,84 22,73 11,72 12,61 3,55 9,46 3,37 12,30 11,19 22,17 26,6 37,10"/></svg><span><sup>$</sup>300</span></div><span class="btn-book">Book Now!</span></article>
  </div>
</section>

<section class="events">
  <h2>Upcoming Events</h2>
  <div class="event-photo" style="left:160px;top:166px;width:209px;height:209px;background:linear-gradient(135deg,#7a5a3a,#3e3a2c)" role="img" aria-label="Photo of a cellist playing outdoors"></div>
  <article class="event-card" style="left:369px;top:166px;width:242px;height:209px">
    <h3>Lorem is simply dummy text</h3>
    <p>Lorem Ipsum is simply dummy text of the printing and typesetting industry, used as standard filler in sample layouts.</p>
    <time>🕒 07/1/2017 | 8:30 pm – 11:00 pm</time>
  </article>
  <div class="event-photo" style="left:160px;top:393px;width:209px;height:217px;background:linear-gradient(180deg,#e0632c,#6a2414 70%,#1a0d08)" role="img" aria-label="Photo of a grand piano silhouetted against a sunset"></div>
  <article class="event-card" style="left:369px;top:393px;width:242px;height:217px">
    <h3>Lorem is simply dummy text</h3>
    <p>Lorem Ipsum is simply dummy text of the printing and typesetting industry, used as standard filler in sample layouts.</p>
    <time>🕒 07/1/2017 | 8:30 pm – 11:00 pm</time>
  </article>
  <div class="event-photo" style="left:633px;top:166px;width:407px;height:264px;background:linear-gradient(135deg,#5f7c45,#2e3a26)" role="img" aria-label="Photo of a pianist playing a white piano in a park"></div>
  <article class="event-card" style="left:633px;top:430px;width:407px;height:180px">
    <h3>Lorem Ipsum is simply dummy text of the printing</h3>
    <p>Lorem Ipsum is simply dummy text of the printing and typesetting industry. It has been the standard dummy text ever since an unknown printer took a galley of type and scrambled it to make a specimen book.</p>
    <time>🕒 07/1/2017 | 8:30 pm – 11:00 pm</time>
  </article>
</section>

<section class="media-row">
  <div class="calendar">
    <div class="cal-head"><i></i><span>March 2017</span><i></i></div>
    <div class="cal-grid">
      <b>MON</b><b>TUE</b><b>WED</b><b>THU</b><b>FRI</b><b>SAT</b><b>SUN</b>
      <span class="off">27</span><span class="off">28</span><span>1</span><span>2</span><span>3</span><span class="on">4</span><span>5</span>
      <span>6</span><span>7</span><span>8</span><span>9</span><span>10</span><span>11</span><span>12</span>
      <span>13</span><span>14</span><span>15</span><span>16</span><span>17</span><span>18</span><span>19</span>
      <span>20</span><span>21</span><span>22</span><span>23</span><span>24</span><span>25</span><span>26</span>
      <span>27</span><span>28</span><span>29</span><span>30</span><span>31</span><span class="off">1</span><span class="off">2</span>
    </div>
  </div>
  <div style="position:absolute;left:435px;top:40px;width:170px;height:270px;background:linear-gradient(135deg,#6f7f52,#3c3526)" role="img" aria-label="Photo of a cellist with her instrument"></div>
  <div class="player">
    <div class="track"><span class="play"></span><div><small>Track Title</small><em>Harlan Reeve – "Riverside Lane"</em></div></div>
    <svg class="wave" width="385" height="50" viewBox="0 0 385 50"><g fill="#9a9a9a"><rect x="0" y="20" width="385" height="14"/></g><g fill="#7d7d7d"><rect x="0" y="14" width="3" height="26"/><rect x="30" y="8" width="3" height="36"/><rect x="60" y="12" width="3" height="30"/><rect x="95" y="6" width="3" height="40"/><rect x="130" y="14" width="3" height="26"/><rect x="170" y="4" width="3" height="44"/><rect x="210" y="10" width="3" height="34"/><rect x="250" y="8" width="3" height="38"/><rect x="290" y="14" width="3" height="26"/><rect x="330" y="6" width="3" height="40"/><rect x="370" y="12" width="3" height="30"/></g></svg>
    <div class="volume">
      <svg width="18" height="16" viewBox="0 0 18 16"><path d="M1 5h4l5-4v14l-5-4H1z" fill="#333"/><path d="M13 4a5 5 0 0 1 0 8" stroke="#333" fill="none" stroke-width="1.5"/></svg>
      <span class="bar"></span>
      <svg width="14" height="16" viewBox="0 0 14 16"><path d="M1 5h4l5-4v14l-5-4H1z" fill="#333"/></svg>
    </div>
  </div>
</section>

<section class="testimonials">
  <h2>TESTIMONIALS</h2>
  <span class="arrow" style="left:160px"></span>
  <span class="arrow" style="left:1016px"></span>
  <div class="avatar" style="left:310px;top:166px;width:144px;height:144px;background:#b79a82" role="img" aria-label="Portrait photo of a client"></div>
  <div class="avatar" style="left:496px;top:135px;width:220px;height:220px;background:#c8a48c" role="img" aria-label="Portrait photo of a smiling client"></div>
  <div class="avatar" style="left:760px;top:166px;width:144px;height:144px;background:#a98b78" role="img" aria-label="Portrait photo of a client"></div>
  <p class="quote">“Lorem Ipsum is simply dummy text of the printing and typesetting industry. Lorem Ipsum has been the industry's standard dummy”<small>(“Lorem Ipsum is simply dummy text of the printing and typesetting industry. Lorem Ipsum has been the industry's standard dummy.)</small></p>
</section>

<footer class="site-footer">
  <h2>SHARE ON</h2>
  <div class="share"><a class="s1" href="#">CIRCLE</a><a class="s2" href="#">CHIRP</a><a class="s3" href="#">SEARCHLY</a></div>
  <div class="tagline">Let's Make Something Great Together</div>
  <div class="contacts"><span>🕒 Mon – Sat: 7:00 – 17:00</span><span>☎ (03) 9021 4418</span><span>✉ hello@tollykessing.com.au</span></div>
  <svg class="pin" width="22" height="32" viewBox="0 0 22 32"><path d="M11 0a11 11 0 0 1 11 11c0 8-11 21-11 21S0 19 0 11A11 11 0 0 1 11 0z" fill="#2f7ec4"/><circle cx="11" cy="11" r="4" fill="#1b1b1b"/></svg>
  <div class="address">212 Linden Row<br>Carlton VIC 3053</div>
  <div class="legal">
    <nav><a href="#">Home</a><a href="#">About Tolly</a><a href="#">Events</a><a href="#">Music</a><a href="#">Video</a><a href="#">Repertoire</a><a href="#">Contact</a></nav>
    <span>© 2017 TOLLYKESSING.COM.AU. ALL RIGHTS RESERVED</span>
  </div>
</footer>

</body>
</html>
```